Anzeigengestaltung für Immobilienmakler für Wohnimmobilien
Zielgruppe
Immobilienmakler für Wohnimmobilien
Aufgabenstellung
Die Maße der Zeitungsanzeige sind 60 mm in der Höhe und 125 in der Breite, Dateiformat ist jpg oder Pdf mit 300dpi.
Bitte eines der zur Verfügung gestellten Logos verwenden
Folgender Text soll in der Anzeige enthalten sein:
Ihr kompetenter Immobilienmakler im Ennepe-Ruhr-Kreis
Lindenweg 7 - 45549 Sprockhövel
Tel. 0202 - 47315526 - www.wohnfeld.de
Optionaler zusätzlicher Text, falls noch Platz in der Anzeige ist:
Gerne bieten wir Ihnen ein unverbindliches Beratungsgespräch, sowie eine
kostenlose Wertermittlung an

```html
<!DOCTYPE html>
<html lang="de">
<head>
<meta charset="utf-8">
<title>Wohnfeld – Immobilienmakler Anzeige</title>
<link href="https://fonts.googleapis.com/css2?family=Cinzel:wght@400;700&family=Montserrat:wght@400;500;700&display=swap" rel="stylesheet">
<style>
  :root {
    --backdrop-light: #f1f2f3;
    --backdrop-mid: #dcdedf;
    --brand-panel: #48474c;
    --brand-ink: #ececec;
    --card-white: #ffffff;
    --heading-ink: #3c3b3f;
    --body-ink: #4a494d;
    --rule: #5a595d;
    --suit-navy: #1f3461;
    --suit-deep: #14244a;
  }
  html, body {
    margin: 0;
    padding: 0;
    overflow: hidden;
  }
  .ad {
    position: relative;
    width: 1200px;
    height: 374px;
    overflow: hidden;
  }
  .ad__backdrop {
    position: absolute;
    inset: 0;
    background: radial-gradient(ellipse at 40% 50%, var(--backdrop-light) 0%, var(--backdrop-mid) 100%);
  }
  .ad__portrait {
    position: absolute;
    left: 737px;
    top: 0;
    width: 463px;
    height: 374px;
    background: linear-gradient(100deg, var(--suit-deep) 0%, var(--suit-navy) 45%, var(--suit-deep) 100%);
    border-top-left-radius: 60px 120px;
  }
  .brand-panel {
    position: absolute;
    left: 68px;
    top: 65px;
    width: 225px;
    height: 249px;
    background: var(--brand-panel);
    display: flex;
    align-items: center;
    justify-content: center;
    gap: 10px;
  }
  .brand-panel__mark {
    width: 14px;
    height: 14px;
    background: var(--brand-ink);
  }
  .brand-panel__name {
    font-family: "Montserrat", sans-serif;
    font-weight: 500;
    font-size: 22px;
    letter-spacing: 0;
    color: var(--brand-ink);
    margin: 0;
  }
  .info-card {
    position: absolute;
    left: 293px;
    top: 65px;
    width: 294px;
    height: 249px;
    background: var(--card-white);
    box-sizing: border-box;
    padding: 20px 0 0 19px;
  }
  .info-card__headline {
    font-family: "Cinzel", serif;
    font-weight: 700;
    font-size: 19px;
    line-height: 23.5px;
    color: var(--heading-ink);
    margin: 0;
  }
  .info-card__contact {
    font-family: "Montserrat", sans-serif;
    font-weight: 400;
    font-size: 12.8px;
    line-height: 18px;
    color: var(--body-ink);
    margin: 9px 0 0;
  }
  .info-card__web {
    font-weight: 700;
  }
  .info-card__rule {
    width: 54px;
    height: 1px;
    background: var(--rule);
    border: 0;
    margin: 19px 0 0;
  }
  .info-card__offer {
    font-family: "Montserrat", sans-serif;
    font-weight: 400;
    font-size: 10px;
    line-height: 18.5px;
    color: var(--body-ink);
    margin: 9px 0 0;
  }
</style>
</head>
<body>
  <div class="ad">
    <div class="ad__backdrop" role="img" aria-label="Unscharfer heller Bürohintergrund"></div>
    <div class="ad__portrait" role="img" aria-label="Geschäftsmann im dunkelblauen Anzug, der seine Krawatte richtet"></div>

    <div class="brand-panel">
      <span class="brand-panel__mark"></span>
      <p class="brand-panel__name">Wohnfeld</p>
    </div>

    <div class="info-card">
      <h1 class="info-card__headline">Ihr kompetenter<br>Immobilienmakler<br>im Ennepe-Ruhr-Kreis</h1>
      <p class="info-card__contact">
        Lindenweg 7 - 45549 Sprockhövel<br>
        0202 - 47315526<br>
        <span class="info-card__web">www.wohnfeld.de</span>
      </p>
      <hr class="info-card__rule">
      <p class="info-card__offer">
        Gerne bieten wir Ihnen ein unverbindliches<br>
        Beratungsgespräch, sowie eine kostenlose<br>
        Wertermittlung an.
      </p>
    </div>
  </div>
</body>
</html>
```